Website Design for new business Junior Stride Athletics

We need a website for our new business Junior Stride Athletics which is about teaching kids from 5 years to 16 years of age how to play either Australian Rules Football or Soccer. Need area for Soccer and Football plus Coaches section, and schedule for each training etc. NEW LOGO ADDED

Target Market(s)

Adults with kids from 5 to 16 looking for specialist coaches to train their kids

Industry/Entity Type

Fitness

Number of Pages Required

5+ page

Colors
3176b5
ffc214

Requirements
Must have
• Logo
• How, Why and What
Nice to have
• I like this website http://www.bramblewickgames.com.au/
• http://www.quillhavenplaydrills.com.au/ is another site that is okay
Should not have
• Our competitor is this website http://www.marrowvaleyouthclinic.com.au/ but I don't like their website style not kid or parent friendly

```html
<!DOCTYPE html>
<html lang="en">
<head>
<meta charset="utf-8">
<title>Junior Stride Athletics – Specialist Sports Coaching</title>
<link rel="stylesheet" href="https://fonts.googleapis.com/css2?family=Oswald:wght@400;500;600;700&family=Roboto+Condensed:wght@400;700&display=swap">
<style>
:root{
  --navy:#262d78;
  --navy-deep:#1f2566;
  --blue:#3176b5;
  --yellow:#ffc214;
  --white:#ffffff;
  --ink:#2b2b2b;
  --muted:#666a73;
  --teal:#16a8a0;
  --teal-dark:#0f8a84;
  --field:#3e9b2c;
  --field-dark:#2c7a1e;
  --pale:#f3f4f6;
}
*{box-sizing:border-box;margin:0;padding:0}
html,body{width:1200px;height:2924px;overflow:hidden;background:var(--white)}
body{position:relative;font-family:"Roboto Condensed",Arial,sans-serif;color:var(--ink)}
.abs{position:absolute}
.heading{font-family:"Oswald",Arial,sans-serif;font-weight:600;color:var(--navy)}
.btn{position:absolute;display:inline-block;font-family:"Oswald",Arial,sans-serif;font-size:14px;font-weight:500;padding:8px 22px;border-radius:3px;text-decoration:none}
.btn-yellow{background:var(--yellow);color:var(--navy)}
.btn-navy{background:var(--navy);color:var(--white)}
.btn-outline{border:1px solid currentColor}
.para{font-size:14px;line-height:1.6;color:var(--muted)}

/* header & hero */
.hero{top:0;left:0;width:1200px;height:500px;background:linear-gradient(180deg,#8fb6dc 0%,#c9dcef 45%,#eef3f8 80%,#ffffff 100%)}
.brand{top:0;left:110px;display:flex;align-items:center;gap:10px;height:80px}
.brand-mark{width:58px;height:80px;background:var(--navy)}
.brand-name{font-family:"Oswald",Arial,sans-serif;font-weight:600;font-size:18px;color:var(--navy)}
.nav{top:34px;left:410px;display:flex;gap:28px;font-family:"Oswald",Arial,sans-serif;font-size:14px;color:var(--navy)}
.nav .active{color:var(--yellow);font-weight:600}
.nav-cta{top:26px;left:920px;padding:7px 18px;border:1px solid var(--navy);border-radius:16px;font-family:"Oswald",Arial,sans-serif;font-size:13px;color:var(--navy);background:rgba(255,255,255,.7)}
.hero-title{top:130px;left:0;width:1200px;text-align:center;font-size:34px}
.hero-sub{top:180px;left:0;width:1200px;text-align:center;font-family:"Oswald",Arial,sans-serif;font-size:18px;color:var(--navy)}
.hero-sub b{color:var(--blue)}
.hero-btn{top:224px;left:530px}
.hero-photo{top:210px;left:380px;width:500px;height:290px;border-radius:6px;background:radial-gradient(ellipse at 50% 60%,rgba(200,70,60,.45),rgba(60,90,140,.25) 55%,rgba(255,255,255,0) 75%)}

/* feature rows */
.why-photo{top:540px;left:150px;width:310px;height:370px;background:linear-gradient(160deg,#3a3a3a,#7b7f86 60%,#d9c37a)}
.why-title{top:620px;left:610px;font-size:30px}
.why-text{top:680px;left:610px;width:400px}
.why-btn{top:800px;left:610px}

.how-band{top:928px;left:0;width:1200px;height:372px;background:linear-gradient(180deg,var(--field) 0%,#4fae37 50%,var(--field-dark) 100%)}
.how-photo{top:960px;left:640px;width:420px;height:340px;background:radial-gradient(ellipse at 50% 55%,rgba(210,50,40,.55),rgba(40,80,170,.35) 50%,rgba(0,0,0,0) 75%)}
.how-title{top:1005px;left:150px;font-size:30px;color:var(--white)}
.how-text{top:1065px;left:150px;width:400px;color:#e9f5e4}
.how-btn{top:1170px;left:150px;color:var(--white)}

.what-photo{top:1340px;left:150px;width:300px;height:400px;background:linear-gradient(170deg,#e8ecef,#cfd5db 50%,#8b9097)}
.what-title{top:1425px;left:610px;font-size:30px}
.what-text{top:1485px;left:610px;width:400px}
.what-btn{top:1585px;left:610px;color:var(--navy)}

/* coaches */
.coaches{top:1760px;left:0;width:1200px;height:360px;background:linear-gradient(180deg,#1c2230 0%,#3b4656 40%,#2d5a2a 75%,#1e3a1c 100%)}
.coaches-title{top:1790px;left:150px;font-size:30px;color:var(--white)}
.coach-photo{top:1890px;left:160px;width:130px;height:130px;border-radius:50%;background:linear-gradient(160deg,#d7b18f,#7a5a46);border:4px solid var(--white)}
.coach-name{top:1880px;left:310px;font-family:"Oswald",Arial,sans-serif;font-size:20px;font-weight:500;color:var(--white)}
.coach-text{top:1916px;left:310px;width:740px;color:#dfe3ea}
.coach-more{top:2025px;left:310px;font-family:"Oswald",Arial,sans-serif;font-size:14px;color:var(--white)}
.arrow{width:28px;height:28px;background:var(--yellow)}
.arrow-left{top:1940px;left:80px}
.arrow-right{top:1940px;left:1060px}

/* special offer */
.offer-title{top:2160px;left:0;width:1200px;text-align:center;font-size:32px}
.offer-card{top:2240px;width:300px;text-align:center}
.offer-card.one{left:300px}
.offer-card.two{left:600px}
.price{margin:0 auto;width:150px;height:150px;border-radius:50%;background:radial-gradient(circle at 40% 35%,#3fd0c5,var(--teal) 55%,var(--teal-dark));display:flex;align-items:center;justify-content:center;font-family:"Oswald",Arial,sans-serif;font-size:42px;font-weight:500;color:var(--white)}
.offer-note{margin-top:22px;font-family:"Oswald",Arial,sans-serif;font-size:15px;color:var(--ink)}
.offer-card .join{position:static;margin-top:14px;color:var(--navy);font-size:13px;padding:6px 20px}

/* fun band */
.fun{top:2520px;left:0;width:1200px;height:240px;background:var(--navy)}
.fun-title{top:2560px;left:150px;font-size:34px;color:var(--white)}
.fun-sub{top:2612px;left:150px;font-family:"Oswald",Arial,sans-serif;font-size:17px;color:#d4d8f2}
.fun-btn{top:2660px;left:150px;border-radius:18px;padding:9px 24px}
.fun-link{top:2668px;left:345px;font-family:"Oswald",Arial,sans-serif;font-size:14px;color:var(--white)}

/* footer */
.footer-line{top:2790px;left:150px;font-family:"Oswald",Arial,sans-serif;font-size:14px;color:var(--navy)}
.footer-line b{color:var(--blue);font-weight:500}
.footer-copy{top:2820px;left:150px;font-size:12px;color:var(--muted)}
.social{top:2790px;left:880px;display:flex;gap:6px}
.social span{width:26px;height:26px;border:1px solid #c7cad3;background:var(--white)}
.social span.on{background:var(--yellow);border-color:var(--yellow)}
.to-top{top:2790px;left:1020px;width:26px;height:26px;background:var(--navy)}
</style>
</head>
<body>

<section class="abs hero" role="img" aria-label="Photo of a bright sky background"></section>
<div class="abs hero-photo" role="img" aria-label="Photo collage of children playing football, soccer, cricket, tennis and basketball"></div>

<header>
  <div class="abs brand"><span class="brand-mark"></span><span class="brand-name">Junior Stride Athletics</span></div>
  <nav class="abs nav">
    <span class="active">Home</span><span>About us</span><span>Our Coaches</span><span>Sources</span><span>News</span><span>Contact Us</span>
  </nav>
  <div class="abs nav-cta">Where Kids are Champions ›</div>
</header>

<h1 class="abs heading hero-title">Specialist Sports Coaching for Boys &amp; Girls 5 to 16 Years Old</h1>
<p class="abs hero-sub">Is your child the next champion? <b>Click here for details »</b></p>
<a class="btn btn-navy hero-btn">Your Week Free Trial</a>

<div class="abs why-photo" role="img" aria-label="Photo of a young American football player in helmet and jersey"></div>
<h2 class="abs heading why-title">Why we do it</h2>
<p class="abs para why-text">We are all about getting kids away from screens and out enjoying a healthy, active life. We aim to teach the skills they need to love their chosen sport, have lots of fun and grow in confidence. Whether your child wants to be a weekend warrior or a future champion, we help them get there.</p>
<a class="btn btn-yellow why-btn">Read More</a>

<section class="abs how-band" role="img" aria-label="Photo of a green grass soccer field"></section>
<div class="abs how-photo" role="img" aria-label="Photo of two young boys playing soccer"></div>
<h2 class="abs heading how-title">How we do it</h2>
<p class="abs para how-text">We start teaching boys and girls from 5 years old basic skills of how to play their chosen sport. We use small groups, experienced coaches, fitness, physical preparation, injury prevention tips and weekly games so every child progresses at their own pace.</p>
<a class="btn btn-outline how-btn">Explore Us</a>

<div class="abs what-photo" role="img" aria-label="Photo of a young cricket batsman in white uniform swinging a bat"></div>
<h2 class="abs heading what-title">What we do</h2>
<p class="abs para what-text">We hold weekly sessions for kids from 5 to 8, 9 to 12 and 13 to 16 years of age. We also have 3 day holiday programs, and for those children that show talent and want to explore their chosen sport further we have elite squads.</p>
<a class="btn btn-outline what-btn">Our Activities</a>

<section class="abs coaches" role="img" aria-label="Photo of a stadium with floodlights at night"></section>
<h2 class="abs heading coaches-title">Coaches – Australian Rule</h2>
<div class="abs arrow arrow-left"><svg width="28" height="28" viewBox="0 0 28 28"><path d="M16 8 L10 14 L16 20" fill="none" stroke="#262d78" stroke-width="2.5"/></svg></div>
<div class="abs arrow arrow-right"><svg width="28" height="28" viewBox="0 0 28 28"><path d="M12 8 L18 14 L12 20" fill="none" stroke="#262d78" stroke-width="2.5"/></svg></div>
<div class="abs coach-photo" role="img" aria-label="Portrait photo of coach Daniel Ferrow"></div>
<h3 class="abs coach-name">Daniel Ferrow</h3>
<p class="abs para coach-text">Daniel Ferrow has played over 200 games of football for his local club and went on to coach at state junior level. He is passionate about helping young players build skills, confidence and a love for the game, and has guided many juniors into senior football.</p>
<span class="abs coach-more">Read More »</span>

<h2 class="abs heading offer-title">Special Offer</h2>
<div class="abs offer-card one">
  <div class="price">$295</div>
  <p class="offer-note">For 8 Sessions Past JSA Participants</p>
  <a class="btn btn-outline join">Join Now</a>
</div>
<div class="abs offer-card two">
  <div class="price">$315</div>
  <p class="offer-note">For 8 Sessions New Enrolments</p>
  <a class="btn btn-outline join">Join Now</a>
</div>

<section class="abs fun"></section>
<h2 class="abs heading fun-title">Have lots of FUN &amp; Help with Personal Development</h2>
<p class="abs fun-sub">Whether your child wants to become a Weekend Warrior or just learn to be a better person!</p>
<a class="btn btn-yellow fun-btn">Our Weekly Clinics</a>
<span class="abs fun-link">Find Nearest Clinic »</span>

<footer>
  <p class="abs footer-line">Have a Question or Enquiry? Email: <b>hello@juniorstride.com.au</b></p>
  <p class="abs footer-copy">Copyright © Junior Stride Athletics 2024 &nbsp;|&nbsp; Privacy Policy</p>
  <div class="abs social"><span></span><span class="on"></span><span></span><span></span></div>
  <div class="abs to-top"><svg width="26" height="26" viewBox="0 0 26 26"><path d="M8 15 L13 10 L18 15" fill="none" stroke="#ffffff" stroke-width="2"/></svg></div>
</footer>

</body>
</html>
```